Bright Paddock Program with the aim of promoting a skills football to school aged children to

Need an A5 back to front one page brochure which is colourful, fun and active to attract the students to purchase the football with part of the funds going back to the school.
Whole idea is to get more footballs in the hands of children of primary school age, fo the school to earn funds from the sale as well as us also making some funds from the sale.
Target Market(s)
5-11 Year old boys and girls
Industry/Entity Type
School
Colors
219ed3
ffffff
0255a3
33b8a4
ec1f27
Requirements
Must have
- Must have football, price, promotional words as per example and contact details of who is ordering the footballs.
- Have included a version we have done up but are not happy with, needs to be much more professional than the attachment to the brief.
Nice to have
- Promotional component on the front with plenty of colours and attraction, with detail requirements on the back
Should not have
- No soccer or KWT balls, only Aussie Rules Footballs in design

```html
<!DOCTYPE html>
<html lang="en">
<head>
<meta charset="utf-8">
<title>Football for School – Order Flyer</title>
<link href="https://fonts.googleapis.com/css2?family=Teko:wght@500;600;700&family=Black+Ops+One&family=Roboto+Condensed:wght@400;700&family=Roboto:wght@400;500&display=swap" rel="stylesheet">
<style>
  :root{
    --red:#ec1f27;
    --red-deep:#b3141b;
    --sky:#219ed3;
    --navy:#0b2a52;
    --turf:#2f6b26;
    --turf-dark:#0d1d0b;
    --panel:#1d1f22;
    --panel-edge:#9aa0a6;
    --silver-hi:#ffffff;
    --silver-lo:#8d939a;
    --white:#ffffff;
    --paper:#f2f2f2;
    --ink:#222222;
  }
  *{margin:0;padding:0;box-sizing:border-box}
  html,body{width:906px;height:1200px;overflow:hidden;background:#ffffff}
  .flyer{position:relative;width:906px;height:1200px;overflow:hidden;background:var(--turf-dark)}

  .stadium-photo{
    position:absolute;inset:0 0 260px 0;
    background:
      radial-gradient(ellipse 60% 35% at 50% 32%, #c23a2e 0%, #9e2219 55%, rgba(158,34,25,0) 80%),
      radial-gradient(ellipse 30% 25% at 8% 28%, rgba(255,255,255,.85), rgba(255,255,255,0) 70%),
      radial-gradient(ellipse 30% 25% at 92% 28%, rgba(255,255,255,.85), rgba(255,255,255,0) 70%),
      linear-gradient(180deg, #0f3e78 0%, #2c7fc0 22%, #4f8fb6 36%, #20303a 52%, var(--turf) 66%, #1f4a1a 84%, var(--turf-dark) 100%);
  }

  .top-tab{
    position:absolute;left:205px;top:0;width:498px;height:40px;
    background:linear-gradient(#2a2a2a,#0e0e0e);
    border:3px solid var(--panel-edge);border-top:none;
    border-radius:0 0 22px 22px;
  }
  .top-tab::after{content:"";position:absolute;left:60px;right:60px;top:18px;height:4px;background:var(--red)}

  .title-panel{position:absolute;left:103px;top:410px;width:700px;height:400px}
  .title-panel svg{position:absolute;inset:0}
  .headline-main{
    position:absolute;left:0;right:0;top:14px;text-align:center;
    font-family:"Teko",sans-serif;font-weight:700;font-size:150px;line-height:1;
    color:var(--red);letter-spacing:2px;
    text-shadow:0 3px 0 var(--red-deep),0 6px 6px rgba(0,0,0,.6);
  }
  .headline-sub{position:absolute;left:60px;top:128px;display:flex;align-items:flex-end;gap:14px}
  .headline-for{font-family:"Black Ops One",sans-serif;font-size:38px;color:#dfe2e5;margin-bottom:18px}
  .headline-school{
    font-family:"Black Ops One",sans-serif;font-size:104px;line-height:1;letter-spacing:4px;
    background:linear-gradient(180deg,var(--silver-hi) 0%,#d7dade 45%,var(--silver-lo) 55%,#e6e8ea 100%);
    -webkit-background-clip:text;background-clip:text;color:transparent;
  }
  .tagline{
    position:absolute;left:86px;top:250px;width:527px;height:37px;
    background:linear-gradient(#1a1a1a,#050505);border:2px solid var(--panel-edge);
    display:flex;align-items:center;justify-content:center;
    font-family:"Black Ops One",sans-serif;font-size:26px;color:#e9ebee;letter-spacing:1px;
  }
  .price{position:absolute;left:0;right:0;top:292px;display:flex;justify-content:center;align-items:flex-start;gap:10px}
  .price-word{font-family:"Teko",sans-serif;font-weight:600;font-size:40px;color:var(--red);line-height:1;margin-top:8px}
  .price-amount{
    font-family:"Black Ops One",sans-serif;font-size:84px;line-height:1;
    background:linear-gradient(180deg,#fff 0%,#d9dcdf 48%,#7f858c 55%,#eceef0 100%);
    -webkit-background-clip:text;background-clip:text;color:transparent;
  }

  .offer-copy{
    position:absolute;left:60px;right:60px;top:846px;text-align:center;
    font-family:"Roboto Condensed",sans-serif;font-size:18px;line-height:23px;color:var(--white);
  }
  .divider{position:absolute;left:240px;right:240px;top:953px;height:1px;background:rgba(255,255,255,.35)}

  .order-form{
    position:absolute;left:51px;top:971px;width:802px;height:183px;
    background:var(--paper);border:2px dashed var(--red);border-radius:8px;
    padding:4px 26px 0;font-family:"Roboto",sans-serif;font-size:15px;color:var(--ink);
  }
  .form-heading{color:var(--red);font-weight:500;font-size:16px;height:29px;line-height:29px}
  .form-row{display:flex;align-items:center;gap:6px;height:29px;line-height:29px;white-space:nowrap}
  .field-line{border-bottom:1px solid #555;height:1px;transform:translateY(6px)}
  .pay-option{display:flex;align-items:center;gap:8px;margin-left:18px}
  .checkbox{width:24px;height:21px;border:1.5px solid #444;border-radius:6px}
  .issuer{
    position:absolute;right:16px;top:100px;width:150px;height:72px;
    display:flex;flex-direction:column;align-items:center;justify-content:center;gap:8px;
    background:#ebebeb;
  }
  .issuer-dot{width:20px;height:20px;border-radius:50%;background:var(--ink)}
  .issuer-name{font-family:"Roboto",sans-serif;font-size:10px;color:var(--ink);text-align:center;line-height:1.2}
  .footnote{
    position:absolute;left:72px;top:1163px;
    font-family:"Roboto Condensed",sans-serif;font-weight:700;font-size:12px;color:var(--red);
  }
</style>
</head>
<body>
<main class="flyer">
  <div class="stadium-photo" role="img" aria-label="Floodlit stadium with three smiling children in red jerseys holding a football and helmet in front of a giant football"></div>
  <div class="top-tab"></div>

  <section class="title-panel">
    <svg viewBox="0 0 700 400" width="700" height="400" aria-hidden="true">
      <path d="M 0 12 L 700 12 L 700 230 L 620 230 L 575 300 L 455 300 L 430 388 L 270 388 L 245 300 L 125 300 L 80 230 L 0 230 Z" fill="#8d939a"/>
      <path d="M 10 22 L 690 22 L 690 222 L 612 222 L 568 292 L 448 292 L 424 380 L 276 380 L 252 292 L 132 292 L 88 222 L 10 222 Z" fill="#1d1f22"/>
      <path d="M 0 110 L 22 130 L 0 150 Z M 700 110 L 678 130 L 700 150 Z" fill="#ffffff"/>
    </svg>
    <h1 class="headline-main">FOOTBALL</h1>
    <div class="headline-sub">
      <span class="headline-for">FOR</span>
      <span class="headline-school">SCHOOL</span>
    </div>
    <p class="tagline">DON’T MISS OUT ON A FOOTBALL</p>
    <p class="price"><span class="price-word">JUST</span><span class="price-amount">$17</span><span class="price-word">EACH</span></p>
  </section>

  <p class="offer-copy">Order your own exclusive* 12″ Skill Football in your local Coastal League club colours and improve your technique this season and help fundraise money for your school. All orders delivered in Term 2 just in time for footy season. $5 from each football purchased will go straight back to your schools P&amp;C!</p>
  <div class="divider"></div>

  <section class="order-form">
    <h2 class="form-heading">ORDER INFORMATION</h2>
    <div class="form-row"><span>Student Name</span><span class="field-line" style="flex:1"></span></div>
    <div class="form-row">
      <span>Year:</span><span class="field-line" style="width:110px"></span>
      <span>Classroom:</span><span class="field-line" style="width:110px"></span>
      <span>Number of footballs:</span><span class="field-line" style="flex:1"></span>
    </div>
    <div class="form-row">
      <span>Payment method:</span>
      <span class="pay-option">Cash <span class="checkbox"></span></span>
      <span class="pay-option">Cheque <span class="checkbox"></span></span>
      <span class="pay-option">EFT <span class="checkbox"></span></span>
    </div>
    <h2 class="form-heading">OFFICE ONLY</h2>
    <div class="form-row"><span>Payment received:</span><span class="field-line" style="width:330px"></span></div>
    <div class="issuer">
      <span class="issuer-dot"></span>
      <span class="issuer-name">Sandgate Footy Commission Inc.</span>
    </div>
  </section>

  <p class="footnote">*Offer only available at selected schools</p>
</main>
</body>
</html>
```